Real Estate For Sale Signage

I'm an independent agent in Lismore NSW Australia with high standards and looking for a catching 'For Sale'sign board.
I like classy, elegant, stylish and simple best.
My colours are red, white and black.
I don't have a logo or other font designs I need to stick to. I like the concept of a house or real estate design.
Before I created this project I played around on publisher and created the PDF attached. I'm not sold on it, but I don't mind the way the name has been layed out. Originally I had a white background with black & red font.
Fancy fonts for my name would be nice, but must not be busy.
Updates

Just wanted to advise that I have updated my brief and used the tools available to help get my ideas through.

Thank you for your work and time.

Kind regards
Marella

Industry/Entity Type

Real Estate

Requirements
Must have
• For Sale
Marella Quint Real Estate (must stand out)
0400 517 382 (must stand out)
17 Tallowood Street North Lismore
www.marellaquintrealestate.com.au

```html
<!DOCTYPE html>
<html lang="en">
<head>
<meta charset="utf-8">
<title>For Sale – Marella Quint Real Estate</title>
<link rel="stylesheet" href="https://fonts.googleapis.com/css2?family=Archivo+Black&family=Arimo:ital,wght@0,700;1,700&display=swap">
<style>
  :root {
    --page: #ffffff;
    --red-deep: #850909;
    --red-mid: #b80000;
    --red-bright: #f20000;
    --brand-red: #a00000;
    --paper: #ffffff;
    --paper-edge: #bdbdbd;
    --ink-light: #f7eeee;
  }
  html, body {
    margin: 0;
    padding: 0;
    width: 1200px;
    height: 900px;
    overflow: hidden;
    background: var(--page);
  }
  .canvas {
    position: relative;
    width: 1200px;
    height: 900px;
  }
  .sign-board {
    position: absolute;
    left: 0;
    top: 0;
  }
  .headline { font-family: "Archivo Black", "Arial Black", sans-serif; font-size: 94px; fill: var(--ink-light); }
  .address { font-family: "Archivo Black", "Arial Black", sans-serif; font-size: 42px; fill: var(--ink-light); }
  .brand-name { fill: var(--brand-red); font-family: "Archivo Black", "Arial Black", sans-serif; }
  .phone { font-family: "Archivo Black", "Arial Black", sans-serif; font-size: 46px; fill: var(--brand-red); }
  .web-address { font-family: "Arimo", Arial, sans-serif; font-weight: 700; font-size: 25px; }
</style>
</head>
<body>
<main class="canvas">
  <svg class="sign-board" width="1200" height="900" viewBox="0 0 1200 900">
    <defs>
      <linearGradient id="boardRed" x1="0" y1="0" x2="0" y2="1">
        <stop offset="0" stop-color="var(--red-deep)"/>
        <stop offset="0.4" stop-color="var(--red-mid)"/>
        <stop offset="1" stop-color="var(--red-bright)"/>
      </linearGradient>
      <radialGradient id="cornerShade" cx="0" cy="0" r="0.6">
        <stop offset="0" stop-color="#000" stop-opacity="0.3"/>
        <stop offset="1" stop-color="#000" stop-opacity="0"/>
      </radialGradient>
      <linearGradient id="paperShade" x1="0" y1="0" x2="1" y2="0">
        <stop offset="0" stop-color="var(--paper)"/>
        <stop offset="0.9" stop-color="var(--paper)"/>
        <stop offset="1" stop-color="var(--paper-edge)"/>
      </linearGradient>
      <filter id="foldShadow" x="-20%" y="-20%" width="140%" height="140%">
        <feDropShadow dx="-4" dy="4" stdDeviation="7" flood-color="#000" flood-opacity="0.5"/>
      </filter>
      <clipPath id="onRed">
        <rect x="305" y="500" width="200" height="390"/>
      </clipPath>
      <clipPath id="onPaper">
        <rect x="505" y="500" width="371" height="390"/>
      </clipPath>
    </defs>

    <rect class="board-field" x="305" y="8" width="571" height="882" fill="url(#boardRed)"/>
    <rect class="board-vignette" x="305" y="8" width="571" height="882" fill="url(#cornerShade)"/>

    <text class="headline" x="338" y="127" textLength="502" lengthAdjust="spacingAndGlyphs">FOR SALE</text>
    <text class="address" x="357" y="202" textLength="465" lengthAdjust="spacingAndGlyphs">17 Tallowood Street</text>
    <text class="address" x="357" y="250">North Lismore</text>

    <polygon class="house-panel" points="345,502 876,204 876,890 505,890 505,502"
             fill="url(#paperShade)" filter="url(#foldShadow)"/>

    <text class="brand-name" font-size="50" transform="translate(478,487) rotate(-29.3) skewX(-12)"
          textLength="430" lengthAdjust="spacingAndGlyphs">Marella Quint</text>
    <text class="brand-name" font-size="37" transform="translate(568,486) rotate(-29.3) skewX(-12)"
          textLength="272" lengthAdjust="spacingAndGlyphs">Real Estate</text>

    <text class="phone" x="690" y="690" text-anchor="middle" textLength="320" lengthAdjust="spacingAndGlyphs">0400 517 382</text>

    <g class="web-address">
      <text x="333" y="845" fill="var(--paper)" clip-path="url(#onRed)"
            textLength="522" lengthAdjust="spacingAndGlyphs">www.marellaquintrealestate.com.au</text>
      <text x="333" y="845" fill="var(--red-bright)" clip-path="url(#onPaper)"
            textLength="522" lengthAdjust="spacingAndGlyphs">www.marellaquintrealestate.com.au</text>
    </g>
  </svg>
</main>
</body>
</html>
```